Business Card Design

We offer full auto repair and auto customization from custom wheels to lift kits and drop kits we do it all. I want something that grabs your attention from the start but nothing flashy i am more of a clean crisp modern kinda of guy. I plan on using the design on my business cards and my main business sign .
Updates
I have up loaded an image of my currant business card designed by me , I would like to improve on it
Target Market(s)
20-35 male and female
Industry/Entity Type
Business
Contact Information for Business Card
Corvello Wheel Works
48362 1/2 Parkfield rd
Brookvale TX, 75512
Manager: Dorian Walsh
P:555-214-7730
F:555-214-7781
Email:Dorian@corvellowheelandgarage.example
website:Corvellowheelandgarage.example
Look and feel

```html
<!DOCTYPE html>
<html lang="en">
<head>
<meta charset="utf-8">
<title>Corvello Wheel Works — Business Card</title>
<link rel="stylesheet" href="https://fonts.googleapis.com/css2?family=Open+Sans:wght@400;600;700&family=Oswald:wght@500&display=swap">
<style>
  :root{
    --bg:#ededed;
    --navy:#1f2a5c;
    --navy-deep:#17204a;
    --navy-band:#243270;
    --orange:#f7a12b;
    --ink:#2b2f3a;
    --muted:#5b6070;
    --white:#ffffff;
  }
  *{margin:0;padding:0;box-sizing:border-box}
  html,body{width:1200px;height:519px;overflow:hidden;background:var(--bg)}
  body{position:relative;font-family:"Open Sans",Arial,sans-serif}

  .card{position:absolute;top:100px;width:540px;height:320px;border-radius:18px;overflow:hidden;box-shadow:0 6px 18px rgba(0,0,0,.18)}

  /* Front */
  .card-front{left:40px;background:var(--white)}
  .brand{position:absolute;top:68px;left:0;width:540px;display:flex;align-items:center;justify-content:center;gap:14px}
  .brand-dot{width:44px;height:44px;border-radius:50%;background:var(--navy);flex:none}
  .brand-name{font-weight:700;color:var(--navy);font-size:27px;line-height:1;letter-spacing:.4px;white-space:nowrap}
  .contact{position:absolute;top:176px;left:0;width:540px;display:flex}
  .person{width:200px;flex:none;text-align:right;padding-right:16px}
  .person-name{font-weight:600;font-size:19px;color:var(--navy)}
  .person-role{font-size:13px;color:var(--muted);margin-top:2px}
  .person-address{font-size:13px;color:var(--ink);margin-top:18px;line-height:1.45}
  .divider{width:3px;height:96px;background:var(--orange);margin-top:2px;flex:none}
  .lines{padding-left:14px;list-style:none}
  .lines li{display:flex;align-items:center;gap:7px;font-size:11.5px;color:var(--ink);height:19px;white-space:nowrap}
  .lines svg{width:12px;height:12px;flex:none}
  .front-band{position:absolute;left:0;bottom:0;width:540px;height:14px;background:var(--orange)}

  /* Back */
  .card-back{left:620px;background:linear-gradient(160deg,var(--navy-band),var(--navy-deep))}
  .tread-band{position:absolute;top:58px;left:0;width:540px;height:64px;background:var(--navy);border-top:2px solid var(--orange);border-bottom:2px solid var(--orange)}
  .tread{position:absolute;top:0;width:38px;height:60px;background:var(--orange)}
  .tread-left{left:0}
  .tread-right{right:0}
  .headline{position:absolute;left:38px;right:38px;top:0;height:60px;display:flex;align-items:center;justify-content:center;font-family:"Oswald",Arial,sans-serif;font-weight:500;font-size:25px;color:var(--orange);letter-spacing:.3px;white-space:nowrap}
  .brands{position:absolute;top:150px;left:40px;width:470px;display:flex;justify-content:space-between}
  .brands ul{list-style:none}
  .brands li{position:relative;padding-left:14px;font-size:9.5px;color:var(--orange);text-transform:uppercase;line-height:17px;white-space:nowrap}
  .brands li::before{content:"";position:absolute;left:0;top:6px;width:5px;height:5px;border-radius:50%;background:var(--orange)}
  .more{position:absolute;top:232px;left:0;width:540px;display:flex;align-items:center;gap:14px}
  .more-rule{height:2px;background:var(--orange)}
  .more-rule.left{width:150px}
  .more-rule.right{flex:1}
  .more-text{font-size:11px;font-weight:600;color:var(--orange);white-space:nowrap}
</style>
</head>
<body>

<section class="card card-front" aria-label="Business card front">
  <div class="brand">
    <span class="brand-dot"></span>
    <div class="brand-name">CORVELLO WHEEL WORKS</div>
  </div>

  <div class="contact">
    <div class="person">
      <p class="person-name">Dorian Walsh</p>
      <p class="person-role">Manager</p>
      <p class="person-address">48362 1/2 Parkfield RD<br>Brookvale TX, 75512</p>
    </div>
    <div class="divider"></div>
    <ul class="lines">
      <li><svg viewBox="0 0 12 12"><rect x="3" y="0.5" width="6" height="11" rx="1.2" fill="none" stroke="#2b2f3a" stroke-width="1.2"/><line x1="5" y1="9.5" x2="7" y2="9.5" stroke="#2b2f3a"/></svg>555-214-7730</li>
      <li><svg viewBox="0 0 12 12"><rect x="1" y="4" width="10" height="6" rx="1" fill="none" stroke="#2b2f3a" stroke-width="1.2"/><rect x="3" y="1" width="6" height="3" fill="none" stroke="#2b2f3a"/><line x1="3" y1="8" x2="9" y2="8" stroke="#2b2f3a"/></svg>555-214-7781</li>
      <li><svg viewBox="0 0 12 12"><rect x="0.8" y="2.5" width="10.4" height="7" fill="none" stroke="#2b2f3a" stroke-width="1.2"/><polyline points="1,3 6,7 11,3" fill="none" stroke="#2b2f3a"/></svg>Dorian@corvellowheelandgarage.example</li>
      <li><svg viewBox="0 0 12 12"><polyline points="1,6 6,1.5 11,6" fill="none" stroke="#2b2f3a" stroke-width="1.2"/><polyline points="2.5,5 2.5,10.5 9.5,10.5 9.5,5" fill="none" stroke="#2b2f3a" stroke-width="1.2"/></svg>www.corvellowheelandgarage.example</li>
    </ul>
  </div>

  <div class="front-band"></div>
</section>

<section class="card card-back" aria-label="Business card back">
  <div class="tread-band">
    <div class="tread tread-left" role="img" aria-label="Tire tread pattern"></div>
    <p class="headline">WE CARRY THE INDUSTRIES FINEST</p>
    <div class="tread tread-right" role="img" aria-label="Tire tread pattern"></div>
  </div>

  <div class="brands">
    <ul>
      <li>Summit Forge</li>
      <li>Crestline Racing</li>
      <li>KTR</li>
      <li>DVL</li>
    </ul>
    <ul>
      <li>QNT</li>
      <li>Halvard XR Series</li>
      <li>Ridgeback Metal</li>
      <li>Ferro Fuel</li>
    </ul>
    <ul>
      <li>Kaveri</li>
      <li>Solenne</li>
      <li>Ashgrove</li>
      <li>Marvane</li>
    </ul>
  </div>

  <div class="more">
    <span class="more-rule left"></span>
    <span class="more-text">AND MANY MORE ...</span>
    <span class="more-rule right"></span>
  </div>
</section>

</body>
</html>
```